Homemaking training schools needs a Business Card design

Designer, Hello!

No special requirements, good-looking enough.
--------------------------------------------------------------------------

Name: Marcus Liao
Chairman
Tel: 0574-57418263
Mobile: 13852247106
Email: kelvory@mailpond.com
Web: www.tqb2031.com
Add: No.258, LinfengJie, DaoyueQu, Ningbo, Zhejiang

LOGO
Ningbo TQB Homemaking Training School

Target Market(s)

pregnant women, mothers, infants, the elderly and families, including cleaning, cooking, nursing training.

Industry/Entity Type

Business

Contact Information for Business Card

Name: Marcus Liao
Chairman
Tel: 0574-57418263
Mobile: 13852247106
Email: kelvory@mailpond.com
Web: www.tqb2031.com

LOGO

Font styles to use
Serif
Sans Serif
Decorative

Requirements
Nice to have
• Feels: clean, specifications, safety, comfort, warmth and happiness.

```html
<!DOCTYPE html>
<html lang="en">
<head>
<meta charset="utf-8">
<title>TianQiBao Business Card</title>
<link rel="stylesheet" href="https://fonts.googleapis.com/css2?family=Arimo:wght@400;700&display=swap">
<style>
  :root {
    --page-bg: #e9e6e1;
    --brand-blue: #1f6fb8;
    --blue-light: #3a8fd6;
    --blue-deep: #12508f;
    --brand-pink: #e3177f;
    --white: #ffffff;
    --text-font: "Arimo", Arial, sans-serif;
  }
  * { box-sizing: border-box; margin: 0; padding: 0; }
  html, body { width: 1200px; height: 950px; overflow: hidden; }
  body {
    background: var(--page-bg);
    font-family: var(--text-font);
    position: relative;
  }
  .card {
    position: absolute;
    left: 260px;
    width: 680px;
    height: 390px;
    box-shadow: 0 10px 28px rgba(0,0,0,0.22);
    overflow: hidden;
  }
  /* Back side */
  .card-back {
    top: 55px;
    background: linear-gradient(135deg, var(--blue-light) 0%, var(--brand-blue) 50%, var(--blue-deep) 100%);
    display: flex;
    flex-direction: column;
    align-items: center;
    justify-content: center;
    color: var(--white);
  }
  .company-name {
    display: flex;
    align-items: center;
    gap: 14px;
    font-weight: 700;
    white-space: nowrap;
  }
  .company-name-back { font-size: 46px; color: var(--white); }
  .company-dot {
    width: 20px; height: 20px; border-radius: 50%;
    background: var(--brand-pink);
    flex: none;
  }
  .back-web {
    margin-top: 40px;
    font-size: 20px;
    letter-spacing: 3px;
    opacity: 0.9;
  }
  /* Front side */
  .card-front {
    top: 500px;
    display: flex;
  }
  .front-name-panel {
    width: 46%;
    background: var(--white);
    display: flex;
    align-items: center;
    justify-content: center;
  }
  .company-name-front { font-size: 36px; color: var(--brand-blue); }
  .front-contact-panel {
    width: 54%;
    background: linear-gradient(160deg, var(--blue-light) 0%, var(--brand-blue) 45%, var(--blue-deep) 100%);
    color: var(--white);
    padding: 44px 40px 0 34px;
    font-size: 17px;
    line-height: 1.3;
  }
  .person-name { font-size: 22px; font-weight: 700; }
  .person-role { margin-bottom: 2px; }
  .divider {
    border: 0;
    border-top: 2px dotted rgba(255,255,255,0.85);
    margin: 12px 0 14px;
    width: 92%;
  }
  .contact-line { display: flex; align-items: center; gap: 10px; }
  .contact-line svg { width: 16px; height: 16px; flex: none; fill: var(--white); }
</style>
</head>
<body>
  <section class="card card-back" aria-label="Card back">
    <div class="company-name company-name-back">
      <span>TianQiBao</span>
      <span class="company-dot"></span>
    </div>
    <p class="back-web">www.tqb2031.com</p>
  </section>

  <section class="card card-front" aria-label="Card front">
    <div class="front-name-panel">
      <div class="company-name company-name-front">
        <span>TianQiBao</span>
        <span class="company-dot"></span>
      </div>
    </div>
    <div class="front-contact-panel">
      <p class="person-name">Marcus Liao</p>
      <p class="person-role">Chairman</p>
      <p>kelvory@mailpond.com</p>
      <hr class="divider">
      <p>No.258, LinfengJie</p>
      <p>DaoyueQu</p>
      <p>Ningbo, Zhejiang</p>
      <hr class="divider">
      <p class="contact-line">
        <svg viewBox="0 0 16 16"><path d="M2 6c0-2 2-3 6-3s6 1 6 3l-3 1-1-2H6L5 7 2 6zM4 8h8l1 6H3z"/></svg>
        0574-57418263
      </p>
      <p class="contact-line">
        <svg viewBox="0 0 16 16"><path d="M4 1h8v14H4zM5.5 3v9h5V3z"/></svg>
        13852247106
      </p>
      <p class="contact-line">
        <svg viewBox="0 0 16 16"><path d="M1 3h14v10H1zM2.5 4.5 8 9l5.5-4.5v-.2H2.5z"/></svg>
        www.tqb2031.com
      </p>
    </div>
  </section>
</body>
</html>
```